Bellwood Tax
Project: Business Cards and Stationery
Business Cards and Stationery - Consulting
Business Cards and Stationery
Modern
Peter Marsh
President
28617 Coralind Ave., 4th Floor Sherman Oaks, CA 90572
peterm@bellwdtax.example
www.bellwoodtaxservice.example

```html
<!DOCTYPE html>
<html lang="en">
<head>
<meta charset="utf-8">
<title>Bellwood Tax — Stationery</title>
<link href="https://fonts.googleapis.com/css2?family=Raleway:wght@400;600&display=swap" rel="stylesheet">
<style>
:root{
  --brand-blue:#3bb0dc;
  --brand-blue-dark:#2a9cc8;
  --ink:#3a3f44;
  --muted:#8a9097;
  --paper:#ffffff;
  --backdrop:#e6e4e1;
  --shadow:0 2px 6px rgba(0,0,0,.18);
}
*{box-sizing:border-box;margin:0;padding:0}
html,body{width:1200px;height:461px;overflow:hidden}
body{background:var(--backdrop);font-family:"Raleway",sans-serif;color:var(--ink);position:relative}
.sheet{position:absolute;background:var(--paper);box-shadow:var(--shadow)}
.wordmark{font-weight:600;letter-spacing:.06em;text-transform:uppercase;color:var(--ink);white-space:nowrap}
.mark-dot{display:inline-block;border-radius:50%;background:var(--brand-blue);vertical-align:middle}
.web{color:#fff;letter-spacing:.14em;font-size:6px;text-transform:lowercase}

/* business cards */
.card{width:96px;height:53px}
.card-front{display:flex;align-items:center;justify-content:center;gap:4px}
.card-front .wordmark{font-size:7px}
.card-front .mark-dot{width:8px;height:8px}
.card-back{padding:6px 7px}
.card-back .name{font-size:6px;font-weight:600}
.card-back .role{font-size:4.5px;color:var(--muted);margin-bottom:3px}
.card-back .line{font-size:3.6px;line-height:1.35;color:var(--ink)}
.card-back .strip{position:absolute;left:0;right:0;bottom:0;height:6px;background:var(--brand-blue)}
.card-tinted{background:#f1f3f4}

/* letterhead */
.letterhead{left:149px;top:19px;width:307px;height:413px}
.letterhead .head{position:absolute;left:26px;top:20px;display:flex;align-items:center;gap:5px}
.letterhead .head .wordmark{font-size:9px}
.letterhead .head .mark-dot{width:10px;height:10px}
.letterhead .contact{position:absolute;left:150px;top:16px;font-size:4.2px;line-height:1.5;color:var(--muted)}
.letterhead .watermark{position:absolute;left:123px;top:155px;width:62px;height:62px;border-radius:50%;background:var(--brand-blue);opacity:.12}
.letterhead .foot{position:absolute;left:0;right:0;bottom:0;height:17px;background:var(--brand-blue);display:flex;align-items:center;justify-content:center}

/* envelopes */
.envelope{left:485px;width:331px;height:108px}
.envelope-open{top:156px}
.envelope-open .flap{position:absolute;left:0;top:0;width:100%;height:34px}
.envelope-open .web{position:absolute;left:0;right:0;top:10px;text-align:center}
.envelope-closed{top:286px}
.envelope-closed .head{position:absolute;left:12px;top:10px;display:flex;align-items:center;gap:4px}
.envelope-closed .head .wordmark{font-size:6px}
.envelope-closed .head .mark-dot{width:7px;height:7px}
.envelope-closed .addr{position:absolute;left:12px;top:22px;font-size:3.8px;line-height:1.4;color:var(--muted)}
.envelope-closed .foot{position:absolute;left:0;right:0;bottom:0;height:12px;background:var(--brand-blue)}

/* presentation folder */
.folder{left:840px;top:19px;width:336px;height:425px}
.folder .centre{position:absolute;left:0;right:0;top:168px;text-align:center}
.folder .centre .mark-dot{width:34px;height:34px;display:block;margin:0 auto 12px}
.folder .centre .wordmark{font-size:23px;font-weight:400;letter-spacing:.05em}
.folder .foot{position:absolute;left:0;right:0;bottom:0;height:19px;background:var(--brand-blue);display:flex;align-items:center;justify-content:center}
</style>
</head>
<body>

<!-- business cards -->
<div class="sheet card card-front card-tinted" style="left:29px;top:96px"><span class="mark-dot"></span><span class="wordmark">Bellwood Tax</span></div>
<div class="sheet card card-back" style="left:29px;top:170px">
  <div class="name">Peter Marsh</div><div class="role">President</div>
  <div class="line">28617 Coralind Ave., 4th Floor</div>
  <div class="line">Sherman Oaks, CA 90572</div>
  <div class="line">(818) 555-0142</div>
  <div class="strip"></div>
</div>
<div class="sheet card card-front" style="left:29px;top:244px"><span class="mark-dot"></span><span class="wordmark">Bellwood Tax</span></div>
<div class="sheet card card-back" style="left:29px;top:318px">
  <div class="name">Peter Marsh</div><div class="role">President</div>
  <div class="line">peterm@bellwdtax.example</div>
  <div class="line">www.bellwoodtaxservice.example</div>
  <div class="line">(818) 555-0142</div>
  <div class="strip"></div>
</div>
<div class="sheet card card-front card-tinted" style="left:29px;top:392px"><span class="mark-dot"></span><span class="wordmark">Bellwood Tax</span></div>

<!-- letterhead -->
<div class="sheet letterhead">
  <div class="head"><span class="mark-dot"></span><span class="wordmark">Bellwood Tax</span></div>
  <div class="contact">
    28617 Coralind Ave., 4th Floor<br>
    Sherman Oaks, CA 90572<br>
    Phone (818) 555-0142<br>
    peterm@bellwdtax.example
  </div>
  <div class="watermark"></div>
  <div class="foot"><span class="web">www.bellwoodtaxservice.example</span></div>
</div>

<!-- envelope, flap open -->
<div class="sheet envelope envelope-open">
  <svg class="flap" viewBox="0 0 331 34" preserveAspectRatio="none" aria-hidden="true">
    <path d="M0 0H331V24Q300 34 260 34H71Q31 34 0 24Z" fill="#3bb0dc"/>
  </svg>
  <div class="web">www.bellwoodtaxservice.example</div>
</div>

<!-- envelope, closed -->
<div class="sheet envelope envelope-closed">
  <div class="head"><span class="mark-dot"></span><span class="wordmark">Bellwood Tax</span></div>
  <div class="addr">28617 Coralind Ave., 4th Floor<br>Sherman Oaks, CA 90572</div>
  <div class="foot"></div>
</div>

<!-- presentation folder -->
<div class="sheet folder">
  <div class="centre"><span class="mark-dot"></span><span class="wordmark">Bellwood Tax</span></div>
  <div class="foot"><span class="web">www.bellwoodtaxservice.example</span></div>
</div>

</body>
</html>
```